Criação de Papelaria Profissional para Imóveis
" BUSCAMOS CLIENTES PARA COMERCIALIZAÇÃO E LOCAÇÃO DE BENS IMÓVEIS, BEM COMO PRESTAMOS SERVIÇOS DE ADMINISTRAÇÃO DE LOCAÇÕES. CONTUDO EMPREGAMOS E BUSCAMOS A EXCELÊNCIA E A SOFISTICAÇÃO EM NOSSA PRESTAÇÃO DE SERVIÇOS. TEMOS QUE SER DIFERENCIADOS, MUITO ACIMA DE MÉDIA E MUITO SOFISTICADOS. "

```html
<!DOCTYPE html>
<html lang="pt-BR">
<head>
<meta charset="utf-8">
<title>Valente &amp; Sampaio — Cartão de Visita</title>
<link rel="stylesheet" href="https://fonts.googleapis.com/css2?family=Montserrat:wght@400;500;600&display=swap">
<style>
  :root {
    --lime: #aac51e;
    --charcoal: #3b3c3e;
    --charcoal-deep: #323335;
    --paper: #ffffff;
    --backdrop: #e4e4e4;
    --text-light: #f2f2f2;
    --text-muted: #c9c9c9;
  }
  * { margin: 0; padding: 0; box-sizing: border-box; }
  html, body { width: 1200px; height: 1200px; overflow: hidden; }
  body {
    background: var(--backdrop);
    font-family: "Montserrat", sans-serif;
    display: flex;
    flex-direction: column;
    align-items: center;
    justify-content: center;
    gap: 70px;
  }
  .card {
    width: 880px;
    height: 490px;
    position: relative;
    overflow: hidden;
    box-shadow: 0 12px 30px rgba(0,0,0,0.18);
  }

  /* Front side */
  .card-front { background: var(--charcoal); }
  .front-header {
    position: absolute; left: 0; top: 0; right: 0; height: 222px;
    background: var(--paper);
    border-bottom: 4px solid var(--lime);
  }
  .brand-lockup {
    position: absolute; left: 270px; top: 78px;
    display: flex; align-items: center; gap: 22px;
  }
  .brand-square {
    width: 56px; height: 56px;
    border: 6px solid var(--lime);
  }
  .brand-divider { width: 2px; height: 64px; background: var(--lime); }
  .brand-text { color: var(--lime); }
  .brand-name {
    font-weight: 500; font-size: 34px; letter-spacing: 2px; text-transform: uppercase;
  }
  .brand-tagline {
    font-weight: 500; font-size: 15px; letter-spacing: 3px; text-transform: uppercase; margin-top: 2px;
  }
  .holder {
    position: absolute; left: 52px; top: 270px;
    border-left: 6px solid var(--lime);
    padding-left: 16px;
    color: var(--text-light);
  }
  .holder-name { font-weight: 500; font-size: 27px; letter-spacing: 0.5px; text-transform: uppercase; }
  .holder-role { font-size: 15px; color: var(--text-muted); margin-top: 2px; }
  .contact-list {
    position: absolute; left: 520px; top: 258px;
    list-style: none; color: var(--text-light);
    font-size: 17px; line-height: 1.2;
  }
  .contact-list li { display: flex; align-items: flex-start; gap: 12px; margin-bottom: 6px; }
  .contact-icon {
    flex: none; width: 18px; height: 18px; margin-top: 2px;
    background: var(--lime); border-radius: 2px;
    display: flex; align-items: center; justify-content: center;
  }
  .contact-icon svg { width: 12px; height: 12px; }

  /* Back side */
  .card-back { background: var(--charcoal); }
  .back-lockup {
    position: absolute; left: 0; right: 0; top: 120px;
    display: flex; flex-direction: column; align-items: center; color: var(--lime);
  }
  .back-lockup .brand-square { width: 90px; height: 90px; border-width: 9px; margin-bottom: 26px; }
  .back-lockup .brand-name { font-size: 46px; letter-spacing: 3px; }
  .back-lockup .brand-tagline { font-size: 20px; letter-spacing: 4px; }
  .back-footer {
    position: absolute; left: 0; right: 0; bottom: 0; height: 86px;
    background: var(--charcoal-deep);
    border-top: 6px solid var(--lime);
  }
  .back-footer::after {
    content: ""; position: absolute; left: 0; right: 0; top: 22px; height: 2px; background: var(--lime);
  }
</style>
</head>
<body>
  <section class="card card-front">
    <header class="front-header">
      <div class="brand-lockup">
        <div class="brand-square"></div>
        <div class="brand-divider"></div>
        <div class="brand-text">
          <div class="brand-name">Valente &amp; Sampaio</div>
          <div class="brand-tagline">Serviços Imobiliários</div>
        </div>
      </div>
    </header>
    <div class="holder">
      <div class="holder-name">Nome e Sobrenome</div>
      <div class="holder-role">Cargo/Função</div>
    </div>
    <ul class="contact-list">
      <li><span class="contact-icon"><svg viewBox="0 0 12 12"><path d="M2.5 1 L4.5 1 L5 3.5 L4 4.5 Q5 7 7.5 8 L8.5 7 L11 7.5 L11 9.5 Q10.5 11 9 11 Q1 10 1 3 Q1 1.5 2.5 1Z" fill="#3b3c3e"/></svg></span>(00) 0000-0000</li>
      <li><span class="contact-icon"><svg viewBox="0 0 12 12"><rect x="1" y="2.5" width="10" height="7" fill="none" stroke="#3b3c3e" stroke-width="1.4"/><path d="M1 2.5 L6 6.5 L11 2.5" fill="none" stroke="#3b3c3e" stroke-width="1.4"/></svg></span>contato@exemplo.com.br</li>
      <li><span class="contact-icon"><svg viewBox="0 0 12 12"><circle cx="6" cy="6" r="4.5" fill="none" stroke="#3b3c3e" stroke-width="1.3"/><path d="M1.5 6 H10.5 M6 1.5 Q3.5 6 6 10.5 M6 1.5 Q8.5 6 6 10.5" fill="none" stroke="#3b3c3e" stroke-width="1"/></svg></span>www.exemplo.com.br</li>
      <li><span class="contact-icon"><svg viewBox="0 0 12 12"><path d="M6 11 Q2 6.5 2 4.5 A4 4 0 0 1 10 4.5 Q10 6.5 6 11Z" fill="#3b3c3e"/><circle cx="6" cy="4.5" r="1.4" fill="#aac51e"/></svg></span><span>rua exemplo, sl 000<br>cidade-UF, CEP: 00000-000</span></li>
    </ul>
  </section>

  <section class="card card-back">
    <div class="back-lockup">
      <div class="brand-square"></div>
      <div class="brand-name">Valente &amp; Sampaio</div>
      <div class="brand-tagline">Serviços Imobiliários</div>
    </div>
    <footer class="back-footer"></footer>
  </section>
</body>
</html>
```